Harbourline Refrigeration business card design

We would like a new design for our business card as we have a new logo.
We need generic business card to give our customers with our office details - with the option of making it individualized for each manager

Target Market(s)

Companies and homeowners

Industry/Entity Type

Air Conditioning

Contact Information for Business Card

We are not sure if we want single or double sided it will depend on the design we choose

Colors
33a6d7
0255a3

Requirements
Must have
• Logo
• phone: (08) 8721 5940
• email: harbourserve@tealnet.example
• website: www.harbourlinerefrigeration.example
• AU61420
• BLD472913
Nice to have
• Address - Shed 5/284 Tallis Rd, Tarrow Bay SA 5611

```html
<!DOCTYPE html>
<html lang="en">
<head>
<meta charset="utf-8">
<title>Harbourline Refrigeration – Business Card</title>
<link rel="stylesheet" href="https://fonts.googleapis.com/css2?family=PT+Sans+Narrow:wght@400;700&family=Open+Sans:wght@400&display=swap">
<style>
  :root {
    --board: #e6e6e6;
    --card: #ffffff;
    --cyan: #4dd3ee;
    --blue: #0f5cf5;
    --navy: #1a40a8;
    --label: #111111;
  }
  html, body {
    margin: 0;
    width: 1200px;
    height: 999px;
    overflow: hidden;
    background: var(--board);
  }
  .board {
    position: relative;
    width: 1285px;
    height: 1070px;
    transform: scale(0.9339);
    transform-origin: 0 0;
    font-family: "PT Sans Narrow", sans-serif;
  }
  .card {
    position: absolute;
    width: 682px;
    height: 379px;
    background: var(--card);
    overflow: hidden;
  }
  .card--front { left: 240px; top: 78px; }
  .card--back  { left: 233px; top: 560px; }
  .stripes {
    position: absolute;
    inset: 0;
    width: 682px;
    height: 379px;
  }
  .stripe { fill: none; stroke-linecap: round; stroke-width: 15; }
  .stripe--cyan { stroke: var(--cyan); }
  .stripe--blue { stroke: var(--blue); }
  .stripe--band { stroke-linecap: butt; stroke-width: 16; }

  .brand {
    position: absolute;
    display: flex;
    align-items: center;
    gap: 12px;
    white-space: nowrap;
  }
  .brand__dot {
    border-radius: 50%;
    background: var(--blue);
    flex: none;
  }
  .brand__name {
    font-weight: 700;
    color: var(--navy);
    letter-spacing: 0.2px;
  }
  .card--front .brand { left: 118px; top: 146px; }
  .card--front .brand__dot { width: 34px; height: 34px; }
  .card--front .brand__name { font-size: 31px; }
  .card--back .brand { left: 150px; top: 168px; }
  .card--back .brand__dot { width: 44px; height: 44px; }
  .card--back .brand__name { font-size: 40px; }

  .website {
    position: absolute;
    right: 48px;
    top: 28px;
    margin: 0;
    font-size: 22px;
    color: var(--cyan);
  }
  .licences {
    position: absolute;
    left: 33px;
    top: 335px;
    margin: 0;
    transform: rotate(-90deg);
    transform-origin: 0 0;
    font-size: 22px;
    color: var(--cyan);
    white-space: nowrap;
    word-spacing: 10px;
  }
  .contact {
    position: absolute;
    left: 380px;
    top: 220px;
    width: 270px;
    margin: 0;
    font-style: normal;
    font-size: 21px;
    line-height: 30px;
    color: var(--cyan);
  }
  .contact__phone { display: block; text-align: center; }
  .contact__email {
    display: block;
    font-weight: 700;
    font-size: 21px;
    color: var(--blue);
    text-align: center;
    margin: 2px 0 4px;
    white-space: nowrap;
  }
  .contact__address { display: block; padding-left: 42px; }

  .label {
    position: absolute;
    margin: 0;
    font-family: "Open Sans", sans-serif;
    font-size: 40px;
    color: var(--label);
  }
  .label--front { left: 1016px; top: 415px; }
  .label--back  { left: 1009px; top: 897px; }
</style>
</head>
<body>
<main class="board">
  <section class="card card--front" aria-label="Business card front">
    <svg class="stripes" viewBox="0 0 682 379" aria-hidden="true">
      <line class="stripe stripe--cyan" x1="472" y1="86" x2="720" y2="218"/>
      <line class="stripe stripe--blue" x1="540" y1="86" x2="720" y2="182"/>
      <line class="stripe stripe--cyan" x1="606" y1="86" x2="720" y2="147"/>
      <line class="stripe stripe--blue" x1="673" y1="86" x2="720" y2="111"/>
      <line class="stripe stripe--cyan" x1="108" y1="215" x2="315" y2="325"/>
      <line class="stripe stripe--blue" x1="108" y1="251" x2="248" y2="325"/>
      <line class="stripe stripe--cyan" x1="108" y1="287" x2="181" y2="325"/>
      <line class="stripe stripe--blue" x1="108" y1="322" x2="112" y2="324"/>
    </svg>
    <p class="website">www.harbourlinerefrigeration.example</p>
    <div class="brand">
      <span class="brand__dot" aria-hidden="true"></span>
      <span class="brand__name">Harbourline Refrigeration</span>
    </div>
    <p class="licences">AU61420 BLD472913</p>
    <address class="contact">
      <span class="contact__phone">(08) 8721 5940</span>
      <span class="contact__email">harbourserve@tealnet.example</span>
      <span class="contact__address">Shed 5/284 Tallis Rd,<br>Tarrow Bay SA 5611</span>
    </address>
  </section>
  <p class="label label--front">Front 1</p>

  <section class="card card--back" aria-label="Business card back">
    <svg class="stripes" viewBox="0 0 682 379" aria-hidden="true">
      <line class="stripe stripe--blue stripe--band" x1="420" y1="-6" x2="700" y2="143"/>
      <line class="stripe stripe--cyan stripe--band" x1="488" y1="-6" x2="700" y2="107"/>
      <line class="stripe stripe--blue stripe--band" x1="556" y1="-6" x2="700" y2="71"/>
      <line class="stripe stripe--cyan stripe--band" x1="624" y1="-6" x2="700" y2="35"/>
      <line class="stripe stripe--blue stripe--band" x1="-20" y1="252" x2="240" y2="390"/>
      <line class="stripe stripe--cyan stripe--band" x1="-20" y1="288" x2="172" y2="390"/>
      <line class="stripe stripe--blue stripe--band" x1="-20" y1="323" x2="105" y2="390"/>
      <line class="stripe stripe--cyan stripe--band" x1="-20" y1="358" x2="38" y2="390"/>
    </svg>
    <div class="brand">
      <span class="brand__dot" aria-hidden="true"></span>
      <span class="brand__name">Harbourline Refrigeration</span>
    </div>
  </section>
  <p class="label label--back">Back</p>
</main>
</body>
</html>
```